Design and put together a 5 page A4 brochure for a Training Programme

Carrowmere Institute of Training deliver a Nationally Accredited Programme in Medical Reception and Administration.

We have a new Qualification (Cert III Business Administration) and we require a 5 page brochure to be designed. (I have CHANGED THIS TO 5 Pages as I can see it is too crowded and not clean enough)

I would put a 6th page in as an application form.

We have recently rebranded our website which is currently under development - so a .jpg will be available of the 'look and feel of this'. I will also upload some stock photos which could be used in the design.

This is an important project for us - so your fantastic work will be greatly appreciated.

This project is fairly urgent - so it is likely we will be choosing a 'winner' to work with sooner rather than later.

Thanks for considering!

I will be uploading various graphics/drafts now.
Updates

Target Market(s)

1/ Women 25-45 yrs undertaking studies in being a medical receptionist
2/ Medical Practices who are hiring Trainees for their medical clinic or hospital

Industry/Entity Type

Medical

Font styles to use
Serif
Sans Serif

Colors
0455a3
fbe7d2
f68e4e
fef4ee
3176b5
33a6d7
f37122

Requirements
Must have
• Clear and clean design - professional
• Graphics of medical pictures (I will supply some so you get the look and feel of wht we are looking for)
• Corporate branding (I will upload a .jpg of new website design for look and feel
• The colour I would like with blue is also a STONE colour - I could not find it in the colour wheel on this site.
• The partner logos should be on the last page probably in one faded colour (such as grey)
Should not have
• I must be able to see the inside of the brochure also, I can not pick this purely on the front cover. Thanks :-)
• I have also now updated the Company Logo

```html
<!DOCTYPE html>
<html lang="en">
<head>
<meta charset="utf-8">
<title>Carrowmere Institute of Training – Brochure Spreads</title>
<link href="https://fonts.googleapis.com/css2?family=PT+Sans+Narrow:wght@700&family=Open+Sans:wght@400;600&display=swap" rel="stylesheet">
<style>
  :root{
    --stage:#8c8c8c;
    --dark:#1b1b1c;
    --dark-2:#2a2a2b;
    --blue:#3a9bd6;
    --blue-deep:#1f7fc0;
    --text:#e9e9e9;
    --muted:#bdbdbd;
    --rule:#4a4a4a;
    --band:#e6e6e6;
    --band-text:#222;
  }
  *{box-sizing:border-box;margin:0;padding:0}
  html,body{width:1200px;height:1000px;overflow:hidden}
  body{background:var(--stage);position:relative;font-family:"Open Sans",Arial,sans-serif;color:var(--text)}
  .page{position:absolute;width:585px;height:413px;overflow:hidden;background:radial-gradient(ellipse at 30% 40%,var(--dark-2),var(--dark) 70%)}
  .page--inside{left:70px;top:80px}
  .page--back{left:542px;top:534px}
  .page svg.shape{position:absolute;left:0;top:0}
  .heading{position:absolute;font-family:"PT Sans Narrow",Arial,sans-serif;font-weight:700;font-size:12.5px;color:#fff;letter-spacing:.1px}
  .heading::after{content:"";display:block;width:110px;height:3px;margin-top:3px;background:var(--rule)}
  .body-text{position:absolute;font-size:5.6px;line-height:8.6px;color:var(--text)}
  .body-text p{margin-bottom:8.6px}
  .package-list{list-style:none}
  .package-list li::before{content:"• "}
  .inset-photo{position:absolute;left:75px;top:35px;width:123px;height:111px;border:4px solid #fff;border-radius:4px;background:linear-gradient(160deg,#f1f4f7,#c9d4de 60%,#e8edf2)}
  .info-band{position:absolute;left:0;top:146px;width:270px;height:78px;background:linear-gradient(90deg,#f0f0f0,#d9d9d9);color:var(--band-text);font-size:5.6px;line-height:10.4px;padding:2px 6px 0 7px}
  .quote{font-style:normal;line-height:13.2px}
  .quote cite{font-style:italic;font-weight:600}
</style>
</head>
<body>

<section class="page page--inside">
  <svg class="shape" width="585" height="413" viewBox="0 0 585 413">
    <defs>
      <linearGradient id="staffPhoto" x1="0" y1="0" x2="1" y2="1">
        <stop offset="0" stop-color="#cfe0e6"/>
        <stop offset=".45" stop-color="#eef3f1"/>
        <stop offset="1" stop-color="#b8c9a8"/>
      </linearGradient>
    </defs>
    <path role="img" aria-label="Photo of two smiling medical reception trainees in white coats" d="M0 0H585V4C470 110 250 178 0 158Z" fill="url(#staffPhoto)"/>
    <path d="M0 158C250 178 470 110 585 4" fill="none" stroke="var(--blue)" stroke-width="9"/>
    <path d="M0 166C250 186 470 118 585 12" fill="none" stroke="var(--blue-deep)" stroke-width="3" opacity=".6"/>
  </svg>

  <h2 class="heading" style="left:18px;top:205px">The student study package – what you receive</h2>
  <ul class="body-text package-list" style="left:18px;top:228px;width:260px">
    <li>Carrowmere Institute Workbook ‘Medical Receptionist and Secretary’s Handbook’</li>
    <li>Carrowmere Institute Workbook ‘Write, Design and Produce Documents for the Australian Medical Office’</li>
    <li>Carrowmere Institute Workbook ‘Medical Triage and Customer Service for non-clinical staff’</li>
    <li>Access to Carrowmere Online Learning platform</li>
    <li>Access to Carrowmere Type-fast programme with testing and certification to Australian standards</li>
    <li>DocuWrite and Layoutly online tutorials and certification</li>
    <li>Digital Medical Transcription Software – student version.</li>
    <li>Medical Accounts Software Clinidesk – demo version to keep</li>
    <li>AMCP endorsed Triage Guide Chart</li>
    <li>Rescue Aid Basic First Aid Booklet and CPR Wallet Card</li>
    <li>CPR Accredited Training</li>
    <li>Cardia Trust endorsed online training programme</li>
    <li>Cardia Trust DVD and Facts Pack for medical professionals</li>
    <li>Access to accredited specialist mentors and trainers</li>
    <li>Registration into Carrowmere’s Job-Network Club</li>
  </ul>

  <h2 class="heading" style="left:319px;top:200px">Unique Delivery Model</h2>
  <div class="body-text" style="left:319px;top:221px;width:250px">
    <p>The Carrowmere Cert III Business Admin (Medical) Programme offers a unique structure to the medical administrative trainee - offering flexibility, intensive face-to-face training of crucial medical units combined with a self-paced home learning and a unique on-line learning programme. This allows studies to be undertaken at a convenient time by students and trainees.</p>
    <p>The programme will adjust to differing skill levels and ability to commit time to the programme and can be completed in as little as 6 months to a maximum of 12 months – depending on prior experience and skills.</p>
    <p>Carrowmere believe some units can only be taught effectively with face to face training led by industry experts and cannot be taught effectively by online learning alone. Therefore Carrowmere’s Core Medical units are taught in workshop settings in 5 Saturdays (or through the week by prior arrangement) followed by self-paced and online delivery of core administration modules. The programme is further followed up with an intensive one day workshop.</p>
    <p>For Traineeships, our Trainers physically attend site 1-2 times for personalised mentoring. There is a mentor/trainer assessor available at all times during our programme for all students.</p>
    <p>All students are invited to Carrowmere’s Computing Medical Software workshop day, where students work hands-on in a workplace simulated environment. Participants receive a complimentary demo copy of a Popular Medical software programme.</p>
  </div>
</section>

<section class="page page--back">
  <svg class="shape" width="585" height="413" viewBox="0 0 585 413">
    <defs>
      <linearGradient id="officePhoto" x1="0" y1="0" x2="1" y2="0">
        <stop offset="0" stop-color="#c7ced6"/>
        <stop offset=".4" stop-color="#f4f6f8"/>
        <stop offset=".75" stop-color="#dfe4ea"/>
        <stop offset="1" stop-color="#aeb8c4"/>
      </linearGradient>
    </defs>
    <path role="img" aria-label="Photo of a businesswoman standing by a bright office window" d="M245 0H585V356C400 320 262 220 245 0Z" fill="url(#officePhoto)"/>
    <path d="M245 0C262 220 400 320 585 356" fill="none" stroke="var(--blue)" stroke-width="9"/>
  </svg>

  <div class="inset-photo" role="img" aria-label="Photo of a team of smiling doctors"></div>

  <div class="info-band">Carrowmere offer a range of training opportunities to Corporates, Hospitals and Industry in either the full qualification or a range of individuals units, including Patient Confidentiality, Medical Terminology, Medical Triage and Customer Service for Non-Clinical Staff. For corporate enquiries, please email info@carrowmeretraining.edu.au. Great incentives are available for employers wanting to sponsor new staff to study the BSB31115 Business Administration (Medical) with bonus employer payments of between $1500 - $5000. Enquire today.</div>

  <h2 class="heading" style="left:18px;top:230px">Funding (Queensland)</h2>
  <div class="body-text" style="left:18px;top:262px;width:252px">
    <p>The Queensland Government will offset the cost of study for eligible students. You will still need to pay for a portion of your study costs.</p>
    <p style="margin-bottom:0">Carrowmere Institute of Training has been chosen by the Department of Education and Training to deliver Government Subsidised Courses through the Certificate 3 Guarantee programme, VET Investment Plan and User Choice initiatives.<br>Therefore Carrowmere Institute are able to offer subsidised training for students who are eligible for the Certificate 3 Guarantee Programme, delivery and manage Traineeships in Cert III Business Administration (Medical) and offer services in Vocational Training for Schools (VETis). For Course and funding opportunities, please contact our office by email or phone to find out more.</p>
  </div>

  <h2 class="heading" style="left:18px;top:366px">Contact us</h2>
  <div class="body-text" style="left:18px;top:387px;width:200px">info@carrowmeretraining.edu.au<br>FREECALL 1800 555 014</div>

  <h2 class="heading" style="left:291px;top:324px">Testimonial</h2>
  <p class="body-text quote" style="left:291px;top:343px;width:244px">“The trainers were excellent in their delivery and knowledge. I want to say a huge thank you to Carrowmere for the course and knowledge I came away with. I have secured a fantastic job after my first application! Such good value for money too! I would highly recommend it. I’m a mature age person so it’s never too late to up-skill yourself to get what you deserve!” - <cite>Dana Whitfield</cite></p>
</section>

</body>
</html>
```